Redesign of TaskHarbor.com website

Our website was initially developed 6+ years ago and has been maintained by several different designers. As a result, it is overly complex, inconsistent format/layout and the content is not well structured/easy to navigate

We need the site redeveloped with a more modern look and feel, simpler content structure and ability to implement new/improved tools, such as: Dynamic Forms, Sales Funnels, Landing Pages, improved metadata of our pages and posts, improved SEO/Page ranking, etc.

We currently use DealRiver CRM, Steady Reach for marketing automation and GridPilot forms. We are investigating Floxen for workflow integration which could extend to our website.

Our current website is developed in WordPress, ideally we will stick with this platform, but we’re happy to consider other CMS' if strongly recommended. We may decide to remove/consolidate some of the pages and/or content as part of this re-design.

We don't want to rebrand (ie change corporate logo, colours scheme etc) as part of this website redevelopment and it is critical that we don't lose our current Page Ranking, SEO rankings, backlink benefits, etc as part of this redevelopment.

Sites we like the feel/design of are: boardwiley.com, tallypoint.com and rankgrove.com

Target Market(s)

Corporate, Enterprise and Government B2B clients.

Coding

Coded - Design and coding required

Number of Pages Required

5+ page

Font styles to use
Sans Serif

Colors
ffffff
ec1f27

Requirements
Must have
• Must retain the majority of content on our existing website (although we may re-write some of it as part of this redesign process).
Nice to have
• See above "Project Description"
Should not have

```html
<!DOCTYPE html>
<html lang="en">
<head>
<meta charset="UTF-8">
<title>TaskHarbor — Your Trusted Advisor</title>
<link href="https://fonts.googleapis.com/css2?family=Poppins:wght@300;400;500;600;700&display=swap" rel="stylesheet">
<style>
:root{
  --red:#ec1f27;
  --white:#ffffff;
  --ink:#1f2330;
  --text:#4a4f5c;
  --muted:#8b909b;
  --hero-bg:#f3f4f7;
  --soft-bg:#f6f7fb;
  --line:#e3e5ea;
  --footer:#1f2431;
  --footer-line:#323848;
  --pink:#f1d6d8;
}
*{margin:0;padding:0;box-sizing:border-box}
html,body{width:1200px;height:4211px;overflow:hidden}
body{font-family:"Poppins",sans-serif;color:var(--ink);background:var(--white);position:relative}
.abs{position:absolute}
.btn{position:absolute;display:flex;align-items:center;justify-content:center;background:var(--red);color:var(--white);font-size:13px;font-weight:500;box-shadow:0 6px 14px rgba(236,31,39,.28)}

/* header + hero */
.hero{position:absolute;left:0;top:0;width:1200px;height:631px;background:var(--hero-bg)}
.brand{position:absolute;display:flex;align-items:center;gap:8px}
.brand-mark{width:26px;height:26px;border-radius:50%;background:var(--red)}
.brand-name{font-size:24px;font-weight:400;color:var(--red);line-height:1}
.brand-tag{font-size:8px;color:var(--muted);margin-top:2px}
.nav{position:absolute;left:500px;top:37px;display:flex;gap:0}
.nav a{font-size:13px;color:var(--ink);text-decoration:none;margin-right:28px}
.nav-contact{left:942px;top:30px;width:95px;height:35px;border-radius:2px}
.hero-title{left:175px;top:180px;font-size:50px;font-weight:600;line-height:58px;color:var(--ink)}
.hero-text{left:175px;top:366px;width:340px;font-size:12.5px;line-height:22px;color:var(--text)}
.hero-cta{left:175px;top:459px;width:174px;height:37px;font-size:12.5px}
.hero-art{left:560px;top:122px;width:560px;height:400px;border-radius:50%;background:radial-gradient(circle at 55% 45%,#ffffff 0%,#fbfbfd 55%,#f7e3e4 100%)}
.dot{position:absolute;border-radius:50%;background:var(--pink)}
.dot-grey{background:#dfe1e6}

/* client strip */
.clients{position:absolute;left:0;top:631px;width:1200px;height:124px;background:#f9fafc}
.client{position:absolute;top:680px;font-size:27px;font-weight:700;color:var(--ink);line-height:36px}
.arrow-sm{position:absolute;width:26px;height:26px;border-radius:50%;background:#e3e5ea;display:flex;align-items:center;justify-content:center}
.strip-line{left:175px;top:755px;width:850px;height:1px;background:var(--line)}

/* advisor */
.advisor-title{left:172px;top:824px;font-size:31px;line-height:37px;font-weight:400;color:var(--ink)}
.advisor-title b{font-weight:600}
.advisor-text{left:172px;top:954px;width:340px;font-size:12px;line-height:22px;color:var(--text)}
.step-num{position:absolute;width:48px;height:48px;border-radius:50%;background:#6d717b;color:var(--white);font-size:16px;display:flex;align-items:center;justify-content:center}
.step-title{position:absolute;font-size:14px;line-height:22px;color:var(--ink)}
.step-text{position:absolute;font-size:12px;line-height:19px;color:var(--text);width:210px}

/* services */
.services-bg{position:absolute;left:0;top:1110px;width:1200px;height:1110px;background:var(--soft-bg)}
.section-title{position:absolute;left:0;width:1200px;text-align:center;font-weight:500}
.svc{position:absolute;width:300px;text-align:center}
.svc h3{font-size:17px;font-weight:400;margin-top:0}
.svc p{font-size:12.5px;line-height:19px;color:var(--text);margin-top:14px}
.svc-card{left:448px;top:1305px;width:301px;height:346px;background:var(--white);box-shadow:0 12px 30px rgba(30,35,60,.08)}
.arrow-lg{position:absolute;width:36px;height:36px;border-radius:50%;background:#e1e3e8;display:flex;align-items:center;justify-content:center}

/* managed */
.managed-img{left:226px;top:1820px;width:403px;height:391px;background:linear-gradient(135deg,#e9d3c2 0%,#5a6f99 45%,#1e3468 80%,#162650 100%);box-shadow:0 18px 40px rgba(20,30,60,.25);z-index:2}
.managed-title{left:721px;top:1918px;font-size:33px;line-height:42px;font-weight:500;color:#2b2f3a}
.managed-text{left:721px;top:2017px;width:300px;font-size:12px;line-height:20px;color:var(--text)}

/* red band */
.safe{position:absolute;left:0;top:2211px;width:1200px;height:474px;background:linear-gradient(160deg,#e52a2f 0%,#d81d24 100%)}
.safe-panel{left:163px;top:2211px;width:874px;height:78px;background:var(--soft-bg)}
.safe-title{top:2350px;font-size:34px;font-weight:600;color:var(--white)}
.safe-sub{top:2410px;font-size:19px;font-weight:300;color:var(--white)}
.safe-text{left:290px;top:2462px;width:620px;text-align:center;font-size:12.5px;line-height:21.5px;color:var(--white)}
.btn-white{position:absolute;background:var(--white);color:var(--ink);display:flex;align-items:center;justify-content:center;gap:30px;font-size:13px;box-shadow:0 6px 16px rgba(0,0,0,.15)}

/* news */
.news-title{left:188px;top:2753px;font-size:31px;font-weight:500}
.news-card{position:absolute;top:2829px;width:262px;height:400px;background:var(--white);box-shadow:0 6px 24px rgba(30,35,60,.1)}
.news-img{position:absolute;left:10px;top:9px;width:242px;height:218px}
.news-date{position:absolute;left:12px;top:251px;font-size:10px;color:var(--text)}
.news-h{position:absolute;left:12px;top:271px;width:220px;font-size:13px;line-height:19px;color:var(--ink)}
.news-p{position:absolute;left:12px;top:316px;width:225px;font-size:11.5px;line-height:17px;color:var(--text)}
.news-meta{position:absolute;left:12px;top:364px;width:238px;display:flex;justify-content:space-between;font-size:10px;color:var(--text)}
.news-meta b{font-weight:500;color:var(--ink)}

/* testimonial */
.testi-bg{position:absolute;left:0;top:3303px;width:1200px;height:494px;background:linear-gradient(180deg,#f1f1f3 0%,#e9e9ec 100%)}
.testi-title{top:3372px;font-size:34px;color:var(--ink)}
.testi-card{left:270px;top:3450px;width:660px;height:245px;background:var(--white);box-shadow:0 10px 30px rgba(30,35,60,.08)}
.quote{left:309px;top:3494px;width:600px;font-size:17.5px;line-height:22px;color:#2b2f3a}
.testi-line{left:300px;top:3584px;width:602px;height:1px;background:#cfd2d8}
.testi-brand{left:314px;top:3612px;font-size:22px;font-weight:600;color:var(--red)}
.testi-name{left:410px;top:3613px;font-size:11px;line-height:18px;color:var(--text)}

/* footer */
.footer{position:absolute;left:0;top:3797px;width:1200px;height:414px;background:var(--footer)}
.foot-about{left:175px;top:3942px;width:240px;font-size:11px;line-height:19px;color:#c8cbd3}
.social{position:absolute;top:4047px;width:32px;height:32px;border-radius:50%;background:#2f3545}
.foot-col{position:absolute;top:3878px}
.foot-col h4{font-size:13px;font-weight:600;color:var(--white);margin-bottom:18px}
.foot-col a{display:block;font-size:11.5px;line-height:29px;color:#8d92a0;text-decoration:none}
.foot-col a.active{color:var(--white);text-decoration:underline}
.foot-rule{left:0;top:4153px;width:1200px;height:1px;background:var(--footer-line)}
.foot-copy{top:4175px;font-size:10px;color:#6f7483}
</style>
</head>
<body>

<!-- header & hero -->
<section class="hero"></section>
<div class="brand" style="left:163px;top:26px">
  <span class="brand-mark"></span>
  <div><div class="brand-name">taskharbor</div><div class="brand-tag">your trusted advisor</div></div>
</div>
<nav class="nav"><a>Home</a><a>Services</a><a>About</a><a>Clients</a><a>Resources</a><a>Blog</a></nav>
<div class="btn nav-contact">Contact</div>

<h1 class="abs hero-title">Next Level,<br>Progress is<br>out Passion!</h1>
<p class="abs hero-text">Our culture is performance driven, We are specialized to help organizations to master "strategic inflections" points in their Company.</p>
<div class="btn hero-cta">CONTACT US TODAY</div>
<div class="abs hero-art" role="img" aria-label="Illustration of two people working with a large analytics dashboard beside a red potted plant"></div>
<span class="dot" style="left:82px;top:324px;width:36px;height:36px"></span>
<span class="dot dot-grey" style="left:1115px;top:189px;width:24px;height:24px"></span>
<span class="dot dot-grey" style="left:495px;top:467px;width:24px;height:24px"></span>

<!-- client strip -->
<section class="clients"></section>
<div class="arrow-sm" style="left:137px;top:685px"><svg width="8" height="10"><path d="M6 1L2 5l4 4" fill="none" stroke="#6d717b" stroke-width="1.5"/></svg></div>
<div class="arrow-sm" style="left:1037px;top:685px"><svg width="8" height="10"><path d="M2 1l4 4-4 4" fill="none" stroke="#6d717b" stroke-width="1.5"/></svg></div>
<span class="client" style="left:195px">Arvanta</span>
<span class="client" style="left:360px;color:#2b4fa0">Lumiq</span>
<span class="client" style="left:545px;font-size:22px;font-weight:500;color:#e0662a">Corvale</span>
<span class="client" style="left:730px;color:var(--red)">Kestrion</span>
<span class="client" style="left:884px;font-size:23px;color:#1d2a4d">Brightmoor</span>
<div class="abs strip-line"></div>

<!-- trusted advisor -->
<h2 class="abs advisor-title"><b>Trusted Advisor</b> For<br>Business Continuity<br>Solutions</h2>
<p class="abs advisor-text">Lorem Ipsum is simply dummy text of the printing and typesetting industry. Lorem Ipsum has been the industry's standard dummy text ever since the 1500s,</p>
<div class="step-num" style="left:598px;top:852px">1</div>
<div class="step-title" style="left:598px;top:920px">Business Continuity<br>Managed Services</div>
<div class="step-text" style="left:598px;top:974px">Lorem Ipsum is simply dummy of the printing and typesetting.</div>
<div class="step-num" style="left:842px;top:852px">2</div>
<div class="step-title" style="left:842px;top:920px">Business Continuity<br>Managed Services</div>
<div class="step-text" style="left:842px;top:974px">Lorem Ipsum is simply dummy of the printing and typesetting.</div>

<!-- what we do -->
<div class="services-bg"></div>
<svg class="abs" style="left:0;top:1090px" width="1200" height="60"><path d="M0 40 C300 0 500 60 800 30 S1100 10 1200 20 V60 H0Z" fill="#f6f7fb"/></svg>
<h2 class="section-title" style="top:1212px;font-size:36px;color:var(--red)">What We DO</h2>

<div class="abs svc-card"></div>
<div class="arrow-lg" style="left:83px;top:1458px"><svg width="10" height="14"><path d="M8 1L2 7l6 6" fill="none" stroke="#6d717b" stroke-width="1.6"/></svg></div>
<div class="arrow-lg" style="left:1079px;top:1458px"><svg width="10" height="14"><path d="M2 1l6 6-6 6" fill="none" stroke="#6d717b" stroke-width="1.6"/></svg></div>

<svg class="abs" style="left:238px;top:1364px" width="66" height="66" viewBox="0 0 66 66" fill="none" stroke="#ec1f27" stroke-width="2">
  <rect x="20" y="4" width="24" height="10" rx="2"/><rect x="20" y="18" width="24" height="10" rx="2"/><rect x="6" y="34" width="34" height="12" rx="2"/>
  <path d="M44 23h8v24"/><circle cx="52" cy="52" r="7" fill="#ec1f27"/><path d="M49 52l2 2 4-4" stroke="#fff"/>
</svg>
<div class="svc" style="left:121px;top:1464px"><h3>Resilience &amp; Continuity</h3><p>Lorem ipsum dolor sit amet,<br>consectetur adipiscing elit, sed<br>do eiusmod tempor.</p></div>

<svg class="abs" style="left:548px;top:1335px" width="100" height="100" viewBox="0 0 100 100">
  <circle cx="50" cy="50" r="50" fill="#6d717b"/>
  <g fill="none" stroke="#fff" stroke-width="2"><path d="M50 30l14 6v10c0 10-6 17-14 20-8-3-14-10-14-20V36z"/><rect x="45" y="46" width="10" height="8"/><path d="M47 46v-4a3 3 0 0 1 6 0v4"/><rect x="26" y="50" width="8" height="8"/><rect x="66" y="50" width="8" height="8"/></g>
</svg>
<div class="svc" style="left:448px;top:1464px"><h3>Security Management</h3><p>Lorem ipsum dolor sit amet,<br>consectetur adipiscing elit, sed<br>do eiusmod tempor.</p></div>
<div class="btn" style="left:515px;top:1576px;width:168px;height:39px;justify-content:space-between;padding:0 22px">Learn More <svg width="8" height="12"><path d="M2 1l5 5-5 5" fill="none" stroke="#fff" stroke-width="1.6"/></svg></div>
<span class="dot" style="left:719px;top:1618px;width:50px;height:50px"></span>

<svg class="abs" style="left:894px;top:1364px" width="66" height="66" viewBox="0 0 66 66" fill="none" stroke="#ec1f27" stroke-width="2">
  <circle cx="33" cy="18" r="8"/><circle cx="33" cy="18" r="3"/><path d="M33 6V2M33 30v4M21 18h-4M45 18h4"/>
  <path d="M33 34v12M20 40v14M46 40v14M27 44v14M39 44v14M20 40h26"/>
</svg>
<div class="svc" style="left:777px;top:1464px"><h3>IT Services &amp; Solutions</h3><p>Lorem ipsum dolor sit amet,<br>consectetur adipiscing elit, sed<br>do eiusmod tempor.</p></div>

<!-- managed continuity -->
<div class="abs managed-img" role="img" aria-label="Photo of a businessman in a suit touching a glowing digital interface"></div>
<h2 class="abs managed-title">Managed Continuity<br>Service</h2>
<p class="abs managed-text">TaskHarbor's business continuity consultant's providing two core services:</p>
<div class="btn" style="left:721px;top:2080px;width:103px;height:34px;font-size:11px">Learn More</div>

<!-- safe band -->
<section class="safe"></section>
<svg class="abs" style="left:0;top:2211px" width="1200" height="474" fill="none" stroke="rgba(255,255,255,.1)" stroke-width="1">
  <path d="M0 60L260 200 420 120 640 300 900 180 1200 260M120 474L260 200 300 20M640 300L700 474M900 180L1000 0M420 120L560 0"/>
</svg>
<div class="abs safe-panel"></div>
<h2 class="section-title safe-title">How To Ensure Your Business Is 100% Safe</h2>
<p class="section-title safe-sub">Your business is only as strong as its weakest link.</p>
<p class="abs safe-text">As an executive in any business, it is understandable that you want to ensure it is 100% safe, because your business is only as strong as its weakest link. You know that if you have a disastrous incident it will cause irreversible damage to your company's good name, your shareholders, board of directors and industry regulators. It will also cause severe legal ramifications.</p>
<div class="btn-white" style="left:515px;top:2580px;width:168px;height:41px">Learn More <svg width="8" height="12"><path d="M2 1l5 5-5 5" fill="none" stroke="#1f2330" stroke-width="1.6"/></svg></div>

<!-- news -->
<h2 class="abs news-title">The Latest News &amp; Information</h2>

<article class="news-card" style="left:175px">
  <div class="news-img" role="img" aria-label="Photo of a laptop surrounded by glowing blue data graphics" style="background:linear-gradient(135deg,#0b3a6e,#1a8fc9 60%,#0d2c55)"></div>
  <div class="news-date">11 February 2018</div>
  <h3 class="news-h">How's Your User Experience for Your Disaster Recovery?</h3>
  <p class="news-p">Lorem ipsum dolor sit amet, elit, sed consectetur adipiscing elit.</p>
  <div class="news-meta"><span>◉ &nbsp;783</span><b>READ MORE</b></div>
</article>
<article class="news-card" style="left:469px">
  <div class="news-img" role="img" aria-label="Photo of a person holding a smartphone with floating cloud icons" style="background:linear-gradient(135deg,#f0ebe6,#c9a891 55%,#7d5a45)"></div>
  <div class="news-date">11 February 2018</div>
  <h3 class="news-h">How's Your User Experience for Your Disaster Recovery?</h3>
  <p class="news-p">Lorem ipsum dolor sit amet, elit, sed consectetur adipiscing elit.</p>
  <div class="news-meta"><span>◉ &nbsp;783</span><b>READ MORE</b></div>
</article>
<article class="news-card" style="left:763px">
  <div class="news-img" role="img" aria-label="Photo of a dark desk with a world map of connected user markers" style="background:linear-gradient(135deg,#2a2d33,#50555e 55%,#15171b)"></div>
  <div class="news-date">11 February 2018</div>
  <h3 class="news-h">How's Your User Experience for Your Disaster Recovery?</h3>
  <p class="news-p">Lorem ipsum dolor sit amet, elit, sed consectetur adipiscing elit.</p>
  <div class="news-meta"><span>◉ &nbsp;783</span><b>READ MORE</b></div>
</article>

<!-- testimonial -->
<section class="testi-bg" role="img" aria-label="Faded photo of a glass office building"></section>
<h2 class="section-title testi-title">Our Client Says</h2>
<div class="abs testi-card"></div>
<p class="abs quote">"It was good to work with you. There are very few true professional organisations such as yours, in this industry. I wish you all the best and I would indeed enjoy working with you again."</p>
<div class="abs testi-line"></div>
<div class="abs testi-brand">Kestrion</div>
<div class="abs testi-name">Daniel Marsh,<br>Head of Infrastructure Services – Kestrion Pacific</div>
<svg class="abs" style="left:190px;top:3582px" width="16" height="24"><path d="M13 2L3 12l10 10" fill="none" stroke="#3b6fe0" stroke-width="2.5"/></svg>
<svg class="abs" style="left:944px;top:3582px" width="16" height="24"><path d="M3 2l10 10-10 10" fill="none" stroke="#3b6fe0" stroke-width="2.5"/></svg>

<!-- footer -->
<footer class="footer"></footer>
<div class="brand" style="left:175px;top:3884px">
  <span class="brand-mark"></span>
  <div><div class="brand-name">taskharbor</div><div class="brand-tag" style="color:#8d92a0">your trusted advisor</div></div>
</div>
<p class="abs foot-about">Why I say old chap that is spiffing bodge, blag pardon me buggered mufty Oxford butty bubble and squeak wind up, brown bread the full monty bloke.</p>
<span class="social" style="left:174px"></span>
<span class="social" style="left:218px;background:var(--red)"></span>
<span class="social" style="left:262px"></span>
<span class="social" style="left:306px"></span>

<div class="foot-col" style="left:515px"><h4>Company</h4><a>Home</a><a>Services</a><a class="active">About Us</a><a>Clients</a><a>Resources</a><a>Blog</a></div>
<div class="foot-col" style="left:683px"><h4>Our Solutions</h4><a>Resilience &amp; Continuity</a><a>Security Management</a><a>IT Services &amp; Solutions</a><a>Data Management</a><a>Software Solutions</a><a>More</a></div>
<div class="foot-col" style="left:901px"><h4>Team Solutions</h4><a>Meet The Team</a><a>Partners</a><a>Faq</a><a>Testimonials</a><a>Sitemap</a><a>See All Teams</a></div>

<div class="abs foot-rule"></div>
<div class="abs foot-copy" style="left:175px">Copyright © 2021 TaskHarbor</div>
<div class="abs foot-copy" style="left:866px">Terms of Use &nbsp;&nbsp; | &nbsp;&nbsp; Privacy Policy</div>

</body>
</html>
```